Business card for senior move management company
@ Project Holder : Could you extend this contest,please?
Is there latitude with the logo, can we remove the wavy lines if they interfere with the design?
All
there are some excellent design choices already, thank you!
General comments are:
1. The client has asked for her name to be in all capitals with the first letter of each word slightly larger than the rest.
2. The client for this company serves are tyically over 75 years old. The fonts need to be clearly legible, and as large as is practical. The phone number is especially important for size.
3. Vhange from the original spec: the website address should go with the text "Organizing, Downsizing and relocation management"
4. the text "Lindenport, MA" should go with the phone number and email.
We are still interested in seeing additional creative ideas.
Thanks Again!
Gareth

```html
<!DOCTYPE html>
<html lang="en">
<head>
<meta charset="utf-8">
<title>GPM Transitions – Business Card</title>
<link href="https://fonts.googleapis.com/css2?family=Arimo:ital,wght@0,400;0,700;1,400;1,700&display=swap" rel="stylesheet">
<style>
  :root {
    --page: #ffffff;
    --card: #ffffff;
    --ink: #111111;
    --brand-deep: #17206b;
    --brand-mid: #2f3f9e;
    --brand-light: #5a6cc8;
    --card-edge: #d7d7d7;
    --shadow: rgba(0,0,0,0.35);
  }
  * { margin: 0; padding: 0; box-sizing: border-box; }
  html, body { width: 1200px; height: 931px; overflow: hidden; background: var(--page); }
  body { position: relative; font-family: "Arimo", Arial, sans-serif; color: var(--ink); }

  .card {
    position: absolute;
    left: 88px;
    width: 675px;
    height: 387px;
    background: var(--card);
    border: 1px solid var(--card-edge);
    border-radius: 30px;
    box-shadow: 0 4px 10px var(--shadow);
    overflow: hidden;
  }
  .card--front { top: 63px; }
  .card--back { top: 483px; }

  .side-label {
    position: absolute;
    font-size: 22px;
    letter-spacing: 0.5px;
  }
  .side-label--front { left: 905px; top: 245px; }
  .side-label--back { left: 908px; top: 655px; }

  .website {
    position: absolute;
    font-weight: 700;
    font-size: 23px;
    white-space: nowrap;
  }
  .card--front .website { left: 37px; top: 40px; }
  .card--back .website { left: 0; right: 0; top: 317px; text-align: center; }

  .brand-mark {
    position: absolute;
    display: flex;
    align-items: center;
    gap: 8px;
    color: var(--brand-mid);
    font-weight: 700;
    font-size: 19px;
    line-height: 1.1;
    white-space: nowrap;
  }
  .brand-mark__dot {
    width: 16px; height: 16px;
    border-radius: 50%;
    background: var(--brand-mid);
    flex: none;
  }
  .card--front .brand-mark { left: 385px; top: 72px; }
  .card--back .brand-mark { left: 0; right: 0; top: 205px; justify-content: center; }

  .contact-panel {
    position: absolute;
    left: 37px; top: 182px;
    width: 300px; height: 155px;
    border-radius: 18px;
    background: linear-gradient(90deg, var(--brand-deep) 0%, var(--brand-mid) 45%, var(--brand-light) 75%, var(--brand-mid) 100%);
    color: #fff;
    padding: 16px 20px;
  }
  .contact-panel__name {
    font-weight: 700;
    font-size: 30px;
    font-variant: small-caps;
    letter-spacing: 0.5px;
    line-height: 1;
    white-space: nowrap;
  }
  .contact-panel__title {
    font-style: italic;
    font-size: 21px;
    margin-top: 4px;
  }
  .contact-panel__phone { font-size: 21px; margin-top: 16px; }
  .contact-panel__email { font-size: 19px; margin-top: 2px; white-space: nowrap; }

  .services {
    position: absolute;
    left: 382px; top: 262px;
    font-style: italic;
    font-size: 19px;
    line-height: 1.35;
    white-space: nowrap;
  }

  .back-band { position: absolute; left: 0; top: 0; }
  .tagline {
    position: absolute;
    left: 0; right: 0; top: 38px;
    text-align: center;
    color: #fff;
    font-style: italic;
    font-weight: 700;
    font-size: 26px;
    line-height: 1.4;
  }
</style>
</head>
<body>
  <section class="card card--front">
    <div class="website">www.GPMtransitions.com</div>
    <div class="brand-mark"><span class="brand-mark__dot"></span><span>Gentle Path Moves</span></div>
    <div class="contact-panel">
      <div class="contact-panel__name">Dana Whitmore</div>
      <div class="contact-panel__title">President</div>
      <div class="contact-panel__phone">555.210.4388</div>
      <div class="contact-panel__email">dana@GPMtransitions.com</div>
    </div>
    <div class="services">Organizing, Downsizing &amp;<br>Relocation Management<br>Lindenport, MA</div>
  </section>
  <div class="side-label side-label--front">FRONT</div>

  <section class="card card--back">
    <svg class="back-band" width="675" height="387" viewBox="0 0 675 387" aria-hidden="true">
      <defs>
        <linearGradient id="bandGradient" x1="0" y1="0" x2="1" y2="0">
          <stop offset="0" stop-color="#17206b"/>
          <stop offset="0.5" stop-color="#5a6cc8"/>
          <stop offset="1" stop-color="#17206b"/>
        </linearGradient>
      </defs>
      <path d="M0 0 H675 V108 L337 158 L0 108 Z" fill="url(#bandGradient)"/>
    </svg>
    <div class="tagline">You and Your Belongings<br>Moved With Care</div>
    <div class="brand-mark"><span class="brand-mark__dot"></span><span>Gentle Path Moves</span></div>
    <div class="website">www.GPMtransitions.com</div>
  </section>
  <div class="side-label side-label--back">BACK</div>
</body>
</html>
```